Website redesign: OLU - Bright Reel Studio

Web Design Brief
I'm looking for a redesign of our website https://www.brightreel.studio/. The website is built with Wix.

We are an AI Video Production Agency named OLU that uses AI-technology to create videos for our clients. We use the platform vormetric.io to generate videos.

Use case:
A financial services company is looking for a way to transform their inhouse training content to video.
They visit brightreel.studio and submit a brief.
Several production packages are presented, and the company selects the one that suits them best. Pricing is agreed upon, and the company provides the necessary scripts and documentation.

As a growing agency, our web page's primary objective is to acquire business leads (companies seeking professional video services) and to communicate our unique AI-driven approach to video production. The landing page will include a form for potential clients to fill out their requirements, as well as a showcase of our AI's capabilities in video production.

We have not yet chosen a color palette, but we are looking for a design that will inspire confidence in our clients while also highlighting the innovative and creative nature of our service. The overall theme should be sleek, modern, and visual, as our core offering is video creation and editing.

Current website:
https://www.brightreel.studio/

Competitors:
https://www.clipforge.pro/
https://pixelbound.ai/
https://www.quillspots.com/vormetric

Inspiration:
https://www.vormetric.io/
https://lumo.co.uk/
https://crispnorth.co/
https://www.bluefennel.com/

Target Market(s)

Director's of training and others who work with video at companies with $10M+ in revenue and 100+ employees.

Industry/Entity Type

Video Services Agency

Coding

Coded - Design and coding required

Number of Pages Required

1 page

Font styles to use
Sans Serif

Requirements
Must have
• Clear CTA and services showcase above the fold. Include "Services" and "Blog" section.
Nice to have
• Reviews / Proof of concept

```html
<!DOCTYPE html>
<html lang="en">
<head>
<meta charset="utf-8">
<title>OLU - Bright Reel Studio · Landing page, variant 1</title>
<link rel="stylesheet" href="https://fonts.googleapis.com/css2?family=Poppins:wght@400;500;600;700&display=swap">
<style>
:root{
  --blue:#1a7ef0;
  --blue-deep:#0f6fe6;
  --blue-bright:#08a6ef;
  --blue-sky:#bfe8f8;
  --navy:#3b4a6b;
  --ink:#2a2f3a;
  --muted:#8d96a6;
  --white:#ffffff;
}
*{box-sizing:border-box;margin:0;padding:0}
html,body{width:1200px;height:2640px;overflow:hidden;background:var(--white)}
body{font-family:"Poppins",sans-serif;color:var(--ink)}
.board{position:relative;width:1200px;height:2640px;background:var(--white)}
.abs{position:absolute}

/* board notes */
.variant{position:absolute;left:53px;top:52px;font-size:17px;font-weight:600;color:var(--navy)}
.note{position:absolute;left:53px;width:136px;background:var(--white);border-radius:8px;box-shadow:0 2px 10px rgba(40,70,120,.12);padding:11px 12px;font-size:7.4px;line-height:1.25;color:var(--ink)}
.note.wide{width:154px}
.note h4{font-size:8.6px;font-weight:500;color:var(--blue);margin-bottom:7px}
.note p+p{margin-top:8px}
.note-link{position:absolute;height:1px;background:var(--blue-bright)}
.note-dot{position:absolute;width:5px;height:5px;border-radius:50%;background:var(--blue-bright)}

/* page */
.page{position:absolute;left:241px;top:33px;width:918px;height:2517px;overflow:hidden;background:var(--white);box-shadow:0 0 12px rgba(0,0,0,.08)}
.page-bg{position:absolute;left:0;top:0}
.header{position:absolute;left:0;top:0;width:918px;height:40px;background:linear-gradient(180deg,var(--blue-deep),#1b8ef5)}
.brand{position:absolute;left:143px;top:7px;display:flex;align-items:center;gap:6px;color:var(--white);font-weight:700;font-size:24px;letter-spacing:1px;line-height:26px}
.brand i{display:block;width:24px;height:24px;border-radius:50%;border:2px solid var(--white)}
.nav{position:absolute;right:182px;top:15px;display:flex;gap:17px;font-size:7.8px;font-weight:500;color:var(--white);letter-spacing:.3px}

.btn{position:absolute;display:flex;align-items:center;justify-content:center;border-radius:14px;font-size:7.6px;font-weight:600;letter-spacing:.3px}
.btn.solid{background:var(--blue);color:var(--white)}
.btn.ghost{border:1px solid var(--white);color:var(--white)}
.btn.outline{border:1px solid var(--blue);color:var(--blue);background:var(--white)}
.btn.light{background:var(--white);color:var(--blue)}

.hero-title{position:absolute;left:144px;top:70px;font-size:23.5px;line-height:26px;font-weight:600;color:var(--blue)}
.hero-copy{position:absolute;left:144px;top:167px;width:265px;font-size:8.6px;line-height:13px}
.hero-copy p{margin-bottom:7px}

.photo{position:absolute;border-radius:50%}
.fill{position:absolute}

.benefit{position:absolute;top:430px;width:174px;height:114px;background:var(--white);border-radius:8px;box-shadow:0 4px 12px rgba(0,40,110,.18);padding:13px 14px}
.benefit svg{display:block;margin-bottom:6px}
.benefit h3{font-size:8.8px;font-weight:500;color:var(--blue);margin-bottom:7px}
.benefit p{font-size:7.2px;line-height:11px;color:var(--muted)}

.light-title{position:absolute;font-size:22px;line-height:28px;font-weight:600;color:var(--white)}
.light-copy{position:absolute;font-size:7.2px;line-height:11px;color:var(--white)}
.light-copy p{margin-bottom:10px}
.tags{position:absolute;left:480px;top:813px;display:flex;gap:8px}
.tags span{border:1px solid rgba(255,255,255,.8);border-radius:4px;padding:3px 5px;font-size:6.2px;color:var(--white)}

.laptop-screen{position:absolute;border:6px solid #1d2230;border-radius:8px 8px 2px 2px}
.laptop-base{position:absolute;height:6px;background:#4a5366;border-radius:0 0 6px 6px}

.section-title{position:absolute;font-size:22px;line-height:28px;font-weight:600;color:var(--blue)}
.body-copy{position:absolute;font-size:7.6px;line-height:11.4px;color:var(--ink)}

.service{position:absolute;width:151px;background:var(--white);border-radius:6px;box-shadow:0 3px 12px rgba(40,70,120,.14);padding:12px 14px}
.service .head{display:flex;gap:8px;align-items:center;margin-bottom:10px}
.service h3{font-size:9.4px;line-height:12px;font-weight:500;color:var(--blue)}
.service p{font-size:7.2px;line-height:11.4px;color:var(--ink)}
.service a{color:var(--blue-bright);text-decoration:none}

.reviews{position:absolute;left:143px;top:1305px;width:598px;height:142px;border-radius:6px;background:linear-gradient(180deg,var(--blue-bright),var(--blue));color:var(--white);text-align:center;padding-top:20px}
.reviews h2{font-size:21px;line-height:28px;font-weight:600;margin-bottom:6px}
.reviews p{font-size:8.4px;line-height:13px;font-weight:500}
.reviews small{display:block;margin-top:10px;font-size:6.6px}
.reviews u{text-decoration:underline}

.post{position:absolute;top:1824px;width:187px;height:238px;background:var(--white);border-radius:6px;box-shadow:0 3px 12px rgba(40,70,120,.14);overflow:hidden}
.post .thumb{height:120px}
.post .txt{padding:9px 11px}
.post h3{font-size:9.8px;line-height:13.5px;font-weight:600;color:var(--blue);margin-bottom:8px}
.post p{font-size:7px;line-height:11px;color:var(--ink)}
.post a{color:var(--blue-bright);text-decoration:none}

.field{position:absolute;border-bottom:1px solid rgba(255,255,255,.85);font-size:7.2px;color:var(--white);padding-bottom:5px}
.social{position:absolute;left:144px;top:2419px;display:flex;gap:12px;align-items:center;color:var(--white);font-size:10px;font-weight:600}
.social .dot{width:9px;height:9px;border-radius:50%;background:var(--white);display:inline-block;margin-right:4px;vertical-align:middle}
.fine{position:absolute;font-size:5.6px;color:var(--white)}
</style>
</head>
<body>
<div class="board">

  <div class="variant">VAR 1</div>

  <div class="note" style="top:205px"><h4>Hero Section</h4><p>Use 3 main benefits and wrote is by 3 paragraphs</p></div>
  <div class="note-link" style="left:179px;top:232px;width:62px"></div><div class="note-dot" style="left:177px;top:230px"></div><div class="note-dot" style="left:239px;top:230px"></div>

  <div class="note" style="top:501px"><h4>Benefits</h4><p>Show user how many safe.</p></div>
  <div class="note-link" style="left:179px;top:528px;width:62px"></div><div class="note-dot" style="left:177px;top:526px"></div><div class="note-dot" style="left:239px;top:526px"></div>

  <div class="note" style="top:748px"><h4>Training Benefits</h4><p>Continue to show</p></div>
  <div class="note-link" style="left:179px;top:775px;width:62px"></div><div class="note-dot" style="left:177px;top:773px"></div><div class="note-dot" style="left:239px;top:773px"></div>

  <div class="note" style="top:824px"><h4>About Laptop</h4><p>I can use white laptops it is just example to show how we can organized.</p></div>

  <div class="note" style="top:1067px"><h4>Services</h4><p>Open all our services</p></div>
  <div class="note-link" style="left:179px;top:1094px;width:62px"></div><div class="note-dot" style="left:177px;top:1092px"></div><div class="note-dot" style="left:239px;top:1092px"></div>

  <div class="note" style="top:1142px"><h4>Contact US btn</h4><p>If we use support you in the end, better to help user to contact us via button.</p></div>

  <div class="note" style="top:1401px"><h4>Review</h4><p>User read services and after - bum REVIEW in studio) Have just 1 - it is good place for testimonial from client.</p></div>
  <div class="note-link" style="left:179px;top:1445px;width:62px"></div><div class="note-dot" style="left:177px;top:1443px"></div><div class="note-dot" style="left:239px;top:1443px"></div>

  <div class="note" style="top:1494px;height:97px"><h4>About review</h4><p>If You want to show review on others pages for example - Better to have min 4 reviews and show it on carousel slider.</p></div>

  <div class="note" style="top:1646px"><h4>Section</h4><p>I do not know how better to call this section. But I move it here. Because this section show project what user read review before. In this way user read review and after see what OLU made for client.</p></div>
  <div class="note-link" style="left:179px;top:1695px;width:62px"></div><div class="note-dot" style="left:177px;top:1693px"></div><div class="note-dot" style="left:239px;top:1693px"></div>

  <div class="note wide" style="top:2245px"><h4>Combine</h4><p>We can combine here 2 in 1.</p></div>
  <div class="note-link" style="left:179px;top:2269px;width:62px"></div><div class="note-dot" style="left:177px;top:2267px"></div><div class="note-dot" style="left:239px;top:2267px"></div>

  <div class="note wide" style="top:2340px"><h4>Input fields</h4><p>I propose to add Upload files fields it is comfortable for client and make easy to explain for client what He/She wants.</p><p>Add agreement for Privacy Policy - I know that sometimes it is necessary to have on site</p></div>

  <div class="note wide" style="top:2493px"><h4>Email Icon</h4><p>Propose to add EMAIL. It is easy way to send user for email box and he will send email. I know many people who prefer to write mail via email box. After all people always safe in draft and back to write. And simple text fields does not have this function.</p></div>

  <main class="page">
    <svg class="page-bg" width="918" height="2517" viewBox="0 0 918 2517" aria-hidden="true">
      <defs>
        <linearGradient id="heroBlue" x1="0" y1="0" x2="0" y2="1">
          <stop offset="0" stop-color="#1582f2"/><stop offset="1" stop-color="#0aa8f0"/>
        </linearGradient>
        <linearGradient id="footBlue" x1="0" y1="0" x2="0" y2="1">
          <stop offset="0" stop-color="#1576ec"/><stop offset="1" stop-color="#0aa4ef"/>
        </linearGradient>
      </defs>
      <path d="M700 150 C760 70 860 40 918 45 L918 300 C840 260 780 230 700 150Z" fill="#bfe8f8"/>
      <path d="M0 318 C60 326 110 334 160 340 C90 342 40 344 0 346Z" fill="#bfe8f8"/>
      <path d="M0 345 C120 312 240 302 340 318 C460 338 520 358 640 350 C760 340 840 298 918 258 L918 885 L0 885Z" fill="url(#heroBlue)"/>
      <rect x="0" y="885" width="918" height="10" fill="#bfe8f8"/>
      <path d="M0 2068 C150 2070 300 2140 450 2148 C610 2156 760 2160 918 2232 L918 2260 L0 2260Z" fill="#bfe8f8"/>
      <path d="M0 2082 C150 2092 300 2165 460 2168 C620 2170 780 2190 918 2250 L918 2510 L0 2510Z" fill="url(#footBlue)"/>
      <rect x="0" y="2510" width="918" height="7" fill="#bfe8f8"/>
    </svg>

    <header class="header">
      <div class="brand"><i></i>OLU</div>
      <nav class="nav"><span>SERVICES</span><span>TRAINING</span><span>MARKETING</span><span>BLOG</span><span>HOW?</span><span>CONTACT</span></nav>
    </header>

    <h1 class="hero-title">Boost Your Business<br>With AI-Driven Video<br>Production</h1>
    <div class="hero-copy">
      <p>Elevate your training and marketing teams with top-quality videos, maximizing efficiency and professionalism.</p>
      <p>Experience the perfect blend of cutting-edge technology and a human touch.</p>
      <p>Take your operations to the next level with OLU today!</p>
    </div>
    <div class="btn solid" style="left:144px;top:267px;width:92px;height:26px">START PROJECT</div>

    <div class="photo" style="left:447px;top:60px;width:292px;height:292px;background:var(--blue-deep)"></div>
    <div class="photo" role="img" aria-label="Video presenter portrait in front of a night city skyline" style="left:470px;top:83px;width:246px;height:246px;background:linear-gradient(160deg,#5a6477,#2e3240 60%,#8a6a58)"></div>
    <svg class="abs" style="left:575px;top:250px" width="38" height="38" viewBox="0 0 38 38" aria-hidden="true"><circle cx="19" cy="19" r="18" fill="#fff"/><path d="M15 12 L26 19 L15 26Z" fill="#1a7ef0"/></svg>

    <div class="benefit" style="left:146px">
      <svg width="28" height="28" viewBox="0 0 28 28" aria-hidden="true"><circle cx="14" cy="14" r="12" fill="none" stroke="#1a7ef0" stroke-width="1.8"/><path d="M14 7 V14 L18 18" fill="none" stroke="#1a7ef0" stroke-width="1.8" stroke-linecap="round"/></svg>
      <h3>Save 80% of your time</h3>
      <p>Your human expert in video edition will be working for you autonomously, saving your teams time.</p>
    </div>
    <div class="benefit" style="left:360px">
      <svg width="30" height="28" viewBox="0 0 30 28" aria-hidden="true"><path d="M3 12 A12 10 0 0 1 27 12 Z" fill="none" stroke="#1a7ef0" stroke-width="1.6"/><path d="M15 2 V10" stroke="#1a7ef0" stroke-width="1.6"/><circle cx="15" cy="20" r="6" fill="none" stroke="#1a7ef0" stroke-width="1.6"/><text x="15" y="23" font-size="8" text-anchor="middle" fill="#1a7ef0" font-family="Poppins,sans-serif">$</text></svg>
      <h3>Save 80% of your budget</h3>
      <p>Forget about long and expensive production costs, you will make better quality videos for less money.</p>
    </div>
    <div class="benefit" style="left:574px">
      <svg width="28" height="28" viewBox="0 0 28 28" aria-hidden="true"><path d="M4 26 V20 M10 26 V16 M16 26 V12 M22 26 V14" stroke="#1a7ef0" stroke-width="1.8"/><path d="M3 14 L11 7 L16 10 L25 3 M20 3 H25 V8" fill="none" stroke="#1a7ef0" stroke-width="1.6"/></svg>
      <h3>Boost your business efficiency</h3>
      <p>You can use video to automate different areas of your business such as Marketing, Training &amp; Onboarding.</p>
    </div>

    <div class="laptop-screen" style="left:167px;top:657px;width:224px;height:152px"></div>
    <div class="fill" role="img" aria-label="Training video thumbnail: presenter beside the title 5 Benefits of using Video in Training" style="left:173px;top:663px;width:212px;height:140px;background:linear-gradient(120deg,#f0a06a,#f6c25a)"></div>
    <div class="laptop-base" style="left:143px;top:809px;width:271px"></div>
    <h2 class="light-title" style="left:480px;top:648px">Training Benefits</h2>
    <div class="light-copy" style="left:480px;top:689px;width:305px">
      <p>OLU - Bright Reel Studio presents the 5 Benefits of using video for training. We offer a unique service that transforms boring documents like powerpoints, PDFs, and static web pages into dynamic and engaging AI videos.</p>
      <p>Our process begins by analysing your existing training materials and identifying key points that can be enhanced through the use of video.</p>
      <p>The process for you it's really simple, you send us the documents or URL and we take care of all the edition work, you will receive the videos ready to use in MP4 format or we can upload them to the platform you need.</p>
    </div>
    <div class="tags"><span>Visual</span><span>Cost-effective</span><span>Better Scalability</span><span>Auditory</span><span>Multisensory learning</span></div>

    <h2 class="section-title" style="left:144px;top:966px">Our Services</h2>
    <div class="body-copy" style="left:144px;top:1006px;width:214px">It is not just about video, it is about a digital strategy. You may want to create a website such as this one, growing your traffic with SEO, or finding new clients using pay advertisement on different platforms such as Linkora, Facetale, Instaloop, and Chirper... it will all depend on where your customers are... and yes, we are here to support you.</div>
    <div class="btn solid" style="left:144px;top:1110px;width:78px;height:24px">CONTACT US</div>

    <div class="service" style="left:414px;top:972px;height:129px">
      <div class="head"><svg width="26" height="26" viewBox="0 0 26 26" aria-hidden="true"><circle cx="13" cy="13" r="11.5" fill="none" stroke="#1a7ef0" stroke-width="1.5"/><path d="M5 9 C9 10 10 14 8 18 M14 3 C13 8 18 10 22 9 M12 23 C14 18 18 17 22 17" fill="none" stroke="#1a7ef0" stroke-width="1.3"/></svg><h3>AI Enhanced<br>Website Creation</h3></div>
      <p>Your expertise and creativity Webmaster will be working with you to create your dream visually stunning website or targeted landing pages that will <a>increase your sales.</a></p>
    </div>
    <div class="service" style="left:586px;top:972px;height:129px">
      <div class="head"><svg width="26" height="26" viewBox="0 0 26 26" aria-hidden="true"><circle cx="13" cy="13" r="11.5" fill="none" stroke="#1a7ef0" stroke-width="1.5"/><path d="M13 5 L8 19 H18 Z M13 5 V13" fill="none" stroke="#1a7ef0" stroke-width="1.3"/></svg><h3>AI Enhanced<br>Copywritting</h3></div>
      <p>Your Copywriter will create stunning texts, blogs post, social media posts, newsletters, articles, and much more with the help of TextPilot that will <a>power up your results.</a></p>
    </div>
    <div class="service" style="left:414px;top:1127px;height:118px">
      <div class="head"><svg width="26" height="26" viewBox="0 0 26 26" aria-hidden="true"><circle cx="13" cy="13" r="11.5" fill="none" stroke="#1a7ef0" stroke-width="1.5"/><circle cx="13" cy="13" r="6.5" fill="none" stroke="#1a7ef0" stroke-width="1.3"/><circle cx="13" cy="13" r="2" fill="#1a7ef0"/></svg><h3>AI Enhanced<br>SEO</h3></div>
      <p>Your SEO will find, target, and measure the results of the keywords using the latest AI SEO tools in the market that will <a>level up your website visitors.</a></p>
    </div>
    <div class="service" style="left:586px;top:1127px;height:118px">
      <div class="head"><svg width="26" height="26" viewBox="0 0 26 26" aria-hidden="true"><circle cx="13" cy="13" r="11.5" fill="none" stroke="#1a7ef0" stroke-width="1.5"/><circle cx="8.5" cy="13" r="1.3" fill="#1a7ef0"/><circle cx="13" cy="13" r="1.3" fill="#1a7ef0"/><circle cx="17.5" cy="13" r="1.3" fill="#1a7ef0"/></svg><h3>AI Enhanced<br>Social Media</h3></div>
      <p>Your Social Media Manager will be posting content, connecting with your audience, and targeting perfect ads <a>to grow your potential customers.</a></p>
    </div>

    <section class="reviews">
      <h2>Reviews</h2>
      <p>I only provided screenshots of my app and its main features.<br>Then OLU's creative process kicked in and the result was a great<br>promo video that I uploaded on PlayMart and AppDock.</p>
      <small><u>Marco Ellison Vale</u> | Senior Droidex &amp; Orbit OS Engineer</small>
    </section>

    <h2 class="section-title" style="left:142px;top:1561px">Marketing</h2>
    <div class="body-copy" style="left:142px;top:1602px;width:265px;font-size:8.2px;line-height:13px">We are really proud to present the new video we created for Marco Ellison Vale that promotes his APP available for both Droidex &amp; Orbit OS. This video will be featured in PlayMart Store &amp; AppDock store with more than 80.000 Downloads on both platforms.</div>
    <div class="laptop-screen" style="left:494px;top:1555px;width:226px;height:160px"></div>
    <div class="fill" role="img" aria-label="App promo video frame: phone screen beside a presenter" style="left:500px;top:1561px;width:214px;height:148px;background:linear-gradient(120deg,#6d5a46,#3d4654 55%,#2b3038)"></div>
    <svg class="abs" style="left:590px;top:1618px" width="34" height="34" viewBox="0 0 34 34" aria-hidden="true"><circle cx="17" cy="17" r="16" fill="#e8e8e8"/><path d="M13 11 L23 17 L13 23Z" fill="#1d2230"/></svg>
    <div class="laptop-base" style="left:471px;top:1715px;width:270px"></div>

    <h2 class="section-title" style="left:140px;top:1782px">Blog</h2>
    <div class="btn outline" style="left:678px;top:1787px;width:60px;height:22px;font-size:7px;font-weight:500">READ ALL</div>
    <article class="post" style="left:140px">
      <div class="thumb" role="img" aria-label="Hands typing at a video editing workstation" style="background:linear-gradient(160deg,#2c3340,#6b6e73)"></div>
      <div class="txt"><h3>Breaking Barriers: Overcoming Limitations With AI-Powered Video Creation</h3><p>This article explores the transformative power of AI-generated videos in capturing attention and keeping viewers engaged throughout the marketing journ... <a>Read More</a></p></div>
    </article>
    <article class="post" style="left:345px">
      <div class="thumb" role="img" aria-label="Abstract 3D render of glowing purple blocks" style="background:linear-gradient(160deg,#d9dde6,#9a7ed6 60%,#c6ccd8)"></div>
      <div class="txt"><h3>Captivating Audiences: How AI-Generated Videos Drive Viewer Engagement</h3><p>In the era of digital marketing, captivating audiences and driving viewer engagement is crucial for businesses to stand out from the competition. This article ex... <a>Read More</a></p></div>
    </article>
    <article class="post" style="left:550px">
      <div class="thumb" role="img" aria-label="Humanoid robot on a stage" style="background:linear-gradient(160deg,#8d8f9a,#cfd1d8)"></div>
      <div class="txt"><h3>The Future Is Here: Exploring The Advancements Of AI In Video Advertising</h3><p>By leveraging artificial intelligence, marketers can create dynamic and personalized video content that resonates with their target audience... <a>Read More</a></p></div>
    </article>

    <h2 class="light-title" style="left:144px;top:2231px">Let's Talk</h2>
    <div class="light-copy" style="left:144px;top:2268px;width:180px;font-size:8.2px;line-height:12.5px">We will contact you shortly, alternatively you can book a free 15 minutes strategy call.</div>
    <div class="btn ghost" style="left:144px;top:2320px;width:74px;height:25px;font-weight:500">BOOK NOW</div>
    <div class="social">
      <span><span class="dot"></span>Linkora</span>
      <svg width="22" height="16" viewBox="0 0 22 16" aria-label="Email"><rect x="1" y="1" width="20" height="14" rx="1" fill="#fff"/><path d="M1 2 L11 9 L21 2" fill="none" stroke="#1576ec" stroke-width="1.6"/></svg>
      <span><span class="dot"></span>Tubecast</span>
    </div>
    <div class="fine" style="left:144px;top:2447px">© 2023 Powered by OLU - Bright Reel Studio</div>

    <h2 class="light-title" style="left:466px;top:2231px">Start Your Project</h2>
    <div class="field" style="left:466px;top:2268px;width:129px">First Name</div>
    <div class="field" style="left:611px;top:2268px;width:130px">Last Name</div>
    <div class="field" style="left:466px;top:2303px;width:129px">Email</div>
    <div class="field" style="left:611px;top:2303px;width:130px">Phone</div>
    <div class="field" style="left:466px;top:2338px;width:275px">Upload File (pdf, docs, jpeg, ppt)</div>
    <div class="field" style="left:466px;top:2366px;width:275px;height:51px;font-size:6.8px">Tell us about your project</div>
    <svg class="abs" style="left:466px;top:2441px" width="10" height="10" viewBox="0 0 10 10" aria-hidden="true"><rect width="10" height="10" rx="1.5" fill="#fff"/><path d="M2 5 L4.2 7.2 L8 3" fill="none" stroke="#1576ec" stroke-width="1.4"/></svg>
    <div class="fine" style="left:487px;top:2443px">I have read &amp; accept the <u>Privacy policy</u></div>
    <div class="btn light" style="left:647px;top:2433px;width:94px;height:26px">GET STARTED</div>
  </main>
</div>
</body>
</html>
```